marble ridge yard works
cards+letter head+envelopes+signs
marble ridge yard works -
Creative Brief
Use specific fonts
you deside
Simple
Lou Kettering
owner/operator
42 willow ave w po box 260 hollowbrook, on k9z 0a1
lou@marbleridge-example.ca
www.marbleridge-example.ca
professional member of greenscape guild. (they have a logo for this)
plain or watermark my log or just my brand mark.

```html
<!DOCTYPE html>
<html lang="en">
<head>
<meta charset="utf-8">
<title>Marble Ridge Yard Works — Stationery</title>
<link href="https://fonts.googleapis.com/css2?family=Montserrat:wght@400;600;700;800&display=swap" rel="stylesheet">
<style>
  :root{
    --bg:#e7e8e6;
    --paper:#ffffff;
    --green-dark:#2f7d2c;
    --green:#4ea33c;
    --green-light:#8cc63f;
    --ink:#1d1d1b;
    --grey:#6b6b6b;
  }
  *{box-sizing:border-box;margin:0;padding:0}
  html,body{width:1200px;height:912px;overflow:hidden}
  body{background:var(--bg);font-family:'Montserrat',Arial,sans-serif;position:relative;color:var(--ink)}
  .sheet{position:absolute;background:var(--paper);box-shadow:0 4px 14px rgba(0,0,0,.18);overflow:hidden}
  .footer-band{position:absolute;left:0;bottom:0;width:100%;display:block}
  .brand{display:flex;align-items:center;gap:6px;color:var(--green-dark);font-weight:800;text-transform:uppercase;letter-spacing:.02em;line-height:1.05}
  .brand-dot{width:12px;height:12px;border-radius:50%;background:var(--green-dark);flex:none}
  .address{color:var(--green);font-size:8px;font-weight:600;line-height:1.4}

  .letterhead{left:40px;top:40px;width:380px;height:492px}
  .letterhead .brand{position:absolute;left:28px;top:30px;font-size:15px;width:220px}
  .letterhead .address{position:absolute;left:28px;top:72px;font-size:7px}

  .envelope{width:440px;height:220px}
  .envelope .brand{position:absolute;left:26px;top:28px;font-size:14px;width:200px}
  .envelope .address{position:absolute;left:26px;top:70px}
  .envelope-plain{left:460px;top:40px}
  .envelope-window{left:460px;top:290px}
  .window{position:absolute;right:26px;top:34px;width:160px;height:58px;border:1px solid #d4d6d3;border-radius:3px;background:#fafafa}

  .compliment{left:460px;top:540px;width:440px;height:200px}
  .compliment .brand{position:absolute;left:26px;top:26px;font-size:14px;width:200px}
  .compliment .address{position:absolute;left:26px;top:100px}
  .compliment-line{position:absolute;right:30px;top:92px;color:var(--green);font-weight:800;font-size:13px;letter-spacing:.04em;text-transform:uppercase}

  .card{width:220px;height:128px}
  .card-front{left:940px;top:40px}
  .card-front .brand{position:absolute;left:12px;top:14px;font-size:10px;width:110px}
  .card-front .brand-dot{width:8px;height:8px}
  .person{position:absolute;left:12px;top:56px}
  .person-name{font-size:10px;font-weight:600;color:var(--green-dark)}
  .person-role{font-size:6px;color:var(--grey)}
  .contact{position:absolute;right:12px;top:12px;text-align:right;font-size:5.5px;color:var(--grey);line-height:1.5}

  .card-back{left:940px;top:190px}
  .member{position:absolute;right:14px;bottom:34px;text-align:right;font-size:7px;color:var(--grey);line-height:1.4}
  .member-site{color:#e08a1e;font-weight:600;font-size:8px}
  .member-badge{position:absolute;right:14px;bottom:8px;width:40px;height:22px;background:#e6efdb;border-radius:3px}
</style>
</head>
<body>
<svg width="0" height="0" style="position:absolute" aria-hidden="true">
  <defs>
    <linearGradient id="band-green" x1="0" y1="0" x2="1" y2="0">
      <stop offset="0" stop-color="#8cc63f"/>
      <stop offset="1" stop-color="#2f7d2c"/>
    </linearGradient>
    <symbol id="footer-band" viewBox="0 0 400 100" preserveAspectRatio="none">
      <path d="M0 70 L400 30 L400 100 L0 100Z" fill="url(#band-green)"/>
    </symbol>
  </defs>
</svg>

<section class="sheet letterhead">
  <div class="brand"><span class="brand-dot"></span>Marble Ridge Yard Works</div>
  <p class="address">42 willow ave w · po box 260 · hollowbrook, on k9z 0a1</p>
  <svg class="footer-band" width="380" height="90"><use href="#footer-band"/></svg>
</section>

<section class="sheet envelope envelope-plain">
  <div class="brand"><span class="brand-dot"></span>Marble Ridge Yard Works</div>
  <p class="address">42 willow ave w po box 260<br>hollowbrook, on k9z 0a1</p>
  <svg class="footer-band" width="440" height="70"><use href="#footer-band"/></svg>
</section>

<section class="sheet envelope envelope-window">
  <div class="brand"><span class="brand-dot"></span>Marble Ridge Yard Works</div>
  <p class="address">42 willow ave w po box 260<br>hollowbrook, on k9z 0a1</p>
  <div class="window"></div>
  <svg class="footer-band" width="440" height="70"><use href="#footer-band"/></svg>
</section>

<section class="sheet compliment">
  <div class="brand"><span class="brand-dot"></span>Marble Ridge Yard Works</div>
  <p class="compliment-line">With Compliment</p>
  <p class="address">42 willow ave w po box 260<br>hollowbrook, on k9z 0a1</p>
  <svg class="footer-band" width="440" height="60"><use href="#footer-band"/></svg>
</section>

<section class="sheet card card-front">
  <div class="brand"><span class="brand-dot"></span>Marble Ridge Yard Works</div>
  <div class="person">
    <p class="person-name">Lou Kettering</p>
    <p class="person-role">owner / operator</p>
  </div>
  <p class="contact">42 willow ave w<br>po box 260<br>hollowbrook, on k9z 0a1<br>Tel. 519 555 0142<br>Cell 519 555 0187<br>Fax 519 555 0163<br>lou@marbleridge-example.ca<br>www.marbleridge-example.ca</p>
  <svg class="footer-band" width="220" height="30"><use href="#footer-band"/></svg>
</section>

<section class="sheet card card-back">
  <p class="member">professional member of<br><span class="member-site">greenscapeguild-example.ca</span></p>
  <div class="member-badge" role="img" aria-label="Greenscape Guild membership badge"></div>
</section>
</body>
</html>
```